Halcyra Gloss: Luxury and Innovation in Eco-Friendly Mobile Car Washing

- Project Overview: Halcyra Gloss is a mobile luxury car wash and disinfection service based in Tunis, Tunisia. We cater to high-end clients and prestigious institutions, offering eco-friendly, on-demand services that combine advanced steam cleaning technology with a sophisticated digital platform for seamless customer experience.
- Design Requirements:
1. Logo Design:
- Style: Elegant, modern, and reflective of luxury and eco-friendliness.
- Elements: Incorporate imagery related to Luxury, car care, cleanliness, and environmental sustainability.
- Color Palette: Preferably gold or silver accents to denote luxury complemented by blues and little greens to signify eco-friendliness.
- Brand Mark Integration: Include the phrase "Powered by Quenbrix Technology (see: https://www.quenbrix-usa.com/)" to highlight our use of advanced equipment.
- Website Design:
- Objective: Create a user-friendly, responsive website that serves as a showcase for our services, emphasizing our commitment to quality and eco-friendliness.
- Features: Service descriptions with high-quality images.
Client testimonials and case studies. Contact information and an interactive map of our service areas.
- Aesthetic: Clean, minimalist design with intuitive navigation, aligning with our brand's luxury and eco-friendly image.
- Brand Mark Placement: Prominently display "Powered by Quenbrix Technology (get inspired from: https://www.quenbrix-usa.com )" on relevant pages to emphasize our use of premium equipment.
- Features:
1. Service descriptions with high-quality images.
2. Client testimonials and case studies.
3. Information on service packages offering attractive pricing for engaged clients.
4. Contact information and an interactive map of our service areas.
- Aesthetic: Clean, minimalist design with intuitive navigation, aligning with our brand's luxury, performant technology, and eco-friendly image.
- Target Audience: High-net-worth individuals owning luxury vehicles.
Prestigious institutions such as hotels, private clinics, and corporate clients seeking premium car care and disinfection services.
Additional Information: Our services emphasize convenience, quality, and environmental responsibility. The design should communicate our commitment to excellence and sustainability, appealing to clients who value premium services and eco-conscious practices. Incorporating the "Powered by Quenbrix Technology" brand mark will further underscore our dedication to utilizing top-tier equipment in delivering exceptional service.
Our services emphasize convenience, quality, and environmental responsibility. The design should communicate our commitment to excellence and sustainability, appealing to clients who value premium services and eco-conscious practices. Incorporating the "Powered by Quenbrix Technology" brand mark will further underscore our dedication to utilizing top-tier equipment in delivering exceptional service.

Target Market(s)

Our target market includes high-net-worth individuals owning luxury vehicles and prestigious institutions such as hotels, private clinics, and corporate clients seeking premium car care and disinfection services.

Industry/Entity Type

Automotive Services / Luxury Services

Coding

Coded - Design and coding required

Number of Pages Required

5+ page

Font styles to use
Sans Serif
Script

Requirements
Must have
• Our project must have: A clean, minimalist design with intuitive navigation. Prominent display of the "Powered by Quenbrix Technology" brand mark. Responsive design for optimal viewing on various devices.
Nice to have
• Interactive elements that enhance user engagement. Animations or transitions that add a touch of sophistication. Integration of social media feeds or links.
Should not have
• Our project must not have: Cluttered layouts or overwhelming visuals. Outdated design elements that do not align with our modern brand image. Slow-loading pages or non-responsive design.

```html
<!DOCTYPE html>
<html lang="en">
<head>
<meta charset="utf-8">
<title>Halcyra Gloss — Luxury Mobile Car Washing</title>
<link rel="stylesheet" href="https://fonts.googleapis.com/css2?family=Roboto:wght@400;500;700;900&family=Libre+Baskerville:wght@700&family=Russo+One&display=swap">
<style>
:root{
  --gold:#b8893a;
  --gold-light:#e8c86b;
  --gold-grad:linear-gradient(90deg,#a87a2e,#d9b25a 55%,#b8893a);
  --blue:#0d5cff;
  --green:#16a00b;
  --ink:#1b1b1b;
  --text:#555;
  --muted:#888;
  --paper:#f1efeb;
  --white:#fff;
  --footer:#141414;
}
*{box-sizing:border-box;margin:0;padding:0}
html,body{width:1200px;height:4159px;overflow:hidden}
body{font-family:"Roboto",sans-serif;color:var(--ink);background:var(--white)}
.page{position:relative;width:1200px;height:4159px;overflow:hidden}
.abs{position:absolute}
.serif{font-family:"Libre Baskerville",serif;font-weight:700;text-transform:uppercase}
.gold{color:var(--gold)}
.btn-gold{position:absolute;display:flex;align-items:center;justify-content:center;gap:8px;background:var(--gold-grad);color:var(--ink);font-weight:700;font-size:15px;text-transform:uppercase;letter-spacing:.3px}
.section-title{position:absolute;left:0;width:1200px;text-align:center;font-size:34px;letter-spacing:.5px}
.title-rule{position:absolute;left:550px;width:100px;height:3px;background:var(--gold-grad)}

/* header */
.header{position:absolute;top:0;left:0;width:1200px;height:84px;background:var(--white);z-index:3}
.logo-tab{position:absolute;left:110px;top:0;width:197px;height:113px;z-index:4}
.logo-name{position:absolute;left:110px;top:70px;width:197px;text-align:center;font-weight:900;font-size:19px;color:var(--blue);z-index:5;letter-spacing:.3px}
.nav{position:absolute;left:375px;top:34px;display:flex;gap:20px;font-size:13px;font-weight:500}
.nav .active{color:var(--blue)}
.phone{position:absolute;left:767px;top:28px;display:flex;align-items:center;gap:12px;font-weight:700;font-size:17px}
.book{left:956px;top:23px;width:134px;height:38px;font-size:13px}

/* hero */
.hero{position:absolute;top:84px;left:0;width:1200px;height:586px}
.hero-photo{position:absolute;inset:0;background:linear-gradient(110deg,#2b2b2b 0%,#4a4a4a 45%,#6d6d6d 70%,#3a3a3a 100%)}
.hero h1{position:absolute;left:110px;top:124px;color:var(--white);font-size:37px;line-height:46px}
.hero .btn-gold{left:113px;top:292px;width:202px;height:54px}

/* services */
.services-title{top:735px}
.svc{position:absolute;top:838px;width:233px;height:284px;border:3px solid var(--gold)}
.svc-label{position:absolute;top:1151px;width:233px;text-align:center;font-weight:700;font-size:18px}

/* about */
.about{position:absolute;top:1244px;left:0;width:1200px;height:681px;background:var(--paper)}
.about-photo{position:absolute;left:111px;top:195px;width:453px;height:404px;border:6px solid var(--white);box-shadow:0 4px 14px rgba(0,0,0,.15);background:linear-gradient(135deg,#7a1a10,#c0532b 50%,#2d2f33)}
.eyebrow{position:absolute;font-size:14px;font-weight:700;color:var(--blue);letter-spacing:.4px}
.about h2{position:absolute;left:636px;top:255px;font-size:29px;line-height:39px}
.about p{position:absolute;left:636px;width:453px;font-size:13.5px;line-height:23px;color:var(--text);text-align:justify}
.about .btn-gold{left:636px;top:528px;width:168px;height:48px}

/* powered */
.powered{position:absolute;top:1925px;left:0;width:1200px;height:380px;background:linear-gradient(90deg,#b38a3c 0%,#d7b45c 35%,#f2dd84 60%,#e6cd74 100%);overflow:hidden}
.powered h2{position:absolute;left:111px;top:68px;font-family:"Russo One",sans-serif;font-weight:400;font-size:31px;line-height:40px;color:var(--ink);text-transform:uppercase}
.powered p{position:absolute;left:111px;top:165px;width:400px;font-size:13.5px;line-height:23px;color:#2a2a2a}
.btn-white{position:absolute;left:111px;top:263px;width:257px;height:44px;background:var(--white);display:flex;align-items:center;justify-content:center;font-weight:700;font-size:14px;text-transform:uppercase}
.partner-badge{position:absolute;left:529px;top:119px;width:144px;height:144px;border-radius:50%;background:var(--white);box-shadow:0 0 0 8px rgba(255,255,255,.4),0 6px 18px rgba(0,0,0,.2);display:flex;align-items:center;justify-content:center;font-weight:700;font-size:17px;color:var(--ink)}

/* packages */
.packages-title{top:2373px}
.pkg{position:absolute;width:307px;background:var(--white);box-shadow:0 2px 14px rgba(0,0,0,.12)}
.pkg-head{position:absolute;left:10px;right:10px;top:10px;height:66px;display:flex;align-items:center;justify-content:center;color:var(--white);font-weight:700;font-size:21px;border-radius:4px;background:var(--green)}
.pkg-head::before{content:"";position:absolute;top:10px;left:50%;width:60px;height:4px;margin-left:-30px;background:var(--white);border-radius:2px}
.pkg.featured .pkg-head{background:var(--gold-grad);color:var(--ink)}
.pkg.featured .pkg-head::before{display:none}
.price{position:absolute;left:0;width:100%;text-align:center;font-weight:700;font-size:30px;color:#d59a24}
.pkg ul{position:absolute;left:30px;list-style:none}
.pkg li{display:flex;align-items:center;gap:12px;height:31px;font-size:14px;color:var(--text)}
.pkg li svg{flex:none}
.buy{position:absolute;left:513px;top:2902px;width:175px;height:44px;border-radius:22px;background:var(--gold-grad);display:flex;align-items:center;justify-content:center;gap:8px;font-weight:700;font-size:14px;text-transform:uppercase}

/* testimonials */
.reviews{position:absolute;top:2960px;left:0;width:1200px;height:569px;background:var(--blue)}
.reviews .section-title{top:170px;color:var(--white)}
.review{position:absolute;top:280px;width:315px;height:208px;background:var(--white);padding:20px}
.stars{display:flex;gap:3px}
.review-mark{position:absolute;right:22px;top:19px;width:16px;height:16px;border-radius:50%;border:3px solid #b6b6b6}
.review p{margin-top:14px;font-size:13px;line-height:22px;color:var(--muted)}
.reviewer{position:absolute;left:20px;top:150px;display:flex;gap:10px;align-items:center}
.avatar{width:36px;height:36px;border-radius:50%;background:linear-gradient(135deg,#c9b7a1,#6a5645)}
.reviewer b{display:block;font-size:14px}
.reviewer span{font-size:11.5px;color:var(--muted)}

/* contact */
.map{position:absolute;left:111px;top:3618px;width:624px;height:379px;border:6px solid var(--white);box-shadow:0 2px 14px rgba(0,0,0,.15);background:linear-gradient(135deg,#ece8df,#e3ddcf 60%,#d9d2bf)}
.contact h2{position:absolute;left:809px;top:3655px;font-size:36px}
.info{position:absolute;left:809px;display:flex;gap:15px}
.info small{display:block;font-size:11.5px;color:var(--green);text-transform:uppercase;margin-bottom:4px}
.info div{font-size:14px;line-height:19px}
.contact .btn-gold{left:811px;top:3936px;width:256px;height:45px;font-size:14px}

/* footer */
.footer{position:absolute;top:4091px;left:0;width:1200px;height:68px;background:var(--footer);color:var(--white);font-size:13.5px}
.footer .copy{position:absolute;left:111px;top:25px}
.footer .copy span{color:var(--blue)}
.footer .follow{position:absolute;right:110px;top:24px;display:flex;align-items:center;gap:10px}
.social{width:14px;height:14px;border-radius:50%;background:var(--white)}
</style>
</head>
<body>
<div class="page">

  <header class="header">
    <nav class="nav">
      <span class="active">Home</span><span>About Us</span><span>Services</span><span>Pricing</span><span>Contact Us</span>
    </nav>
    <div class="phone">
      <svg width="28" height="28" viewBox="0 0 28 28"><path d="M14 1l11 5v8c0 7-5 11-11 13C8 25 3 21 3 14V6z" fill="var(--green)"/><path d="M10 9c1-1 2 0 2.5 1.5s-1 1.5-.5 2.5 2 2.5 3 3 1.2-1.2 2.5-.6 2.2 1.3 1.3 2.3c-2 2-5 0-7-2s-3.5-5-1.8-6.7z" fill="#fff"/></svg>
      (555) 214 7730
    </div>
    <div class="btn-gold book">Book Today</div>
  </header>
  <svg class="logo-tab" viewBox="0 0 197 113"><polygon points="0,0 197,0 197,84 182,113 15,113 0,84" fill="#fff"/></svg>
  <div class="logo-name">HALCYRA GLOSS</div>

  <section class="hero">
    <div class="hero-photo" role="img" aria-label="Gloved hand steam cleaning a car dashboard"></div>
    <svg class="abs" style="left:0;top:0" width="1200" height="586">
      <polygon points="0,436 600,566 1200,436 1200,586 0,586" fill="#a9a9a9"/>
      <polygon points="0,450 600,580 1200,450 1200,586 0,586" fill="#fff"/>
    </svg>
    <h1 class="serif">Luxury and Innovation<br>in Eco-Friendly Mobile<br>Car Washing</h1>
    <div class="btn-gold">Get Started
      <svg width="15" height="15" viewBox="0 0 16 16"><circle cx="8" cy="8" r="8" fill="var(--ink)"/><path d="M6 4.5L9.5 8 6 11.5" stroke="#fff" stroke-width="2" fill="none"/></svg>
    </div>
  </section>

  <h2 class="section-title serif services-title"><span class="gold">Our</span> Services</h2>
  <div class="title-rule" style="top:785px"></div>

  <div class="svc" style="left:111px;background:linear-gradient(160deg,#8a7a6a,#c29a62 55%,#5a4a40)" role="img" aria-label="Technician cleaning a door foot panel"></div>
  <div class="svc" style="left:359px;background:linear-gradient(160deg,#6a6a6a,#3a3a3a 50%,#c8652c 70%,#2a2a2a)" role="img" aria-label="Steam nozzle cleaning an engine"></div>
  <div class="svc" style="left:607px;background:linear-gradient(160deg,#3a3a3a,#1a1a1a 55%,#4a4a4a)" role="img" aria-label="Steam jet cleaning a black carpet"></div>
  <div class="svc" style="left:854px;background:linear-gradient(160deg,#8aa070,#9a9a9a 45%,#4a4a4a)" role="img" aria-label="Technician steam cleaning leather seats"></div>
  <div class="svc-label" style="left:111px">Door Foot Panel</div>
  <div class="svc-label gold" style="left:359px">Engine Cleaning</div>
  <div class="svc-label" style="left:607px">Steam Carpets</div>
  <div class="svc-label" style="left:854px">Leather Seats</div>

  <section class="about">
    <svg class="abs" style="left:0;top:0" width="1200" height="140">
      <polygon points="0,0 600,134 1200,0" fill="var(--blue)"/>
      <polygon points="0,-4 600,124 1200,-4" fill="#fff"/>
    </svg>
    <div class="about-photo" role="img" aria-label="Gloved hand holding a steam gun inside a red car"></div>
    <div class="eyebrow" style="left:636px;top:217px">ABOUT HALCYRA GLOSS</div>
    <div class="abs" style="left:838px;top:225px;width:85px;height:2px;background:var(--gold)"></div>
    <h2 class="serif"><span class="gold">Mobile Luxury Car Wash</span><br>and Disinfection Service</h2>
    <p style="top:348px">Lorem ipsum dolor sit amet, consectetur adipiscing elit, sed do eius­mod tempor incididunt ut labore et dolore magna aliqua.</p>
    <p style="top:404px">Ut enim ad minim veniam, quis nostrud exercitation ullamco laboris nisi ut aliquip ex ea commodo consequat. Duis aute irure dolor in repre­henderit in voluptate velit esse cillum dolore eu fugiat nulla pariatur. Ex qui officia deserunt mollit anim id est laborum.</p>
    <div class="btn-gold">Learn More</div>
  </section>

  <section class="powered">
    <svg class="abs" style="left:0;top:0" width="1200" height="380">
      <defs><linearGradient id="van" x1="0" x2="1" y1="0" y2="1"><stop offset="0" stop-color="#c9cbcd"/><stop offset=".5" stop-color="#6c6e72"/><stop offset="1" stop-color="#2c2e31"/></linearGradient></defs>
      <polygon points="670,0 1200,0 1200,380 522,380" fill="url(#van)" role="img" aria-label="Open van carrying orange steam cleaning equipment"/>
    </svg>
    <h2>Powered by Quenbrix<br>Technology</h2>
    <p>Sed ut perspiciatis unde omnis natus error voluptatem accusantium doloremque laudantium, totam rem aperiam, beatae vitae dicta sunt explicabo.</p>
    <div class="btn-white">Schedule an Appointment</div>
    <div class="partner-badge">Quenbrix</div>
  </section>

  <h2 class="section-title serif packages-title"><span class="gold">Service</span> Packages</h2>
  <div class="title-rule" style="top:2423px"></div>

  <div class="pkg" style="left:113px;top:2484px;height:423px">
    <div class="pkg-head">CLASSIC</div>
    <div class="price" style="top:96px">$130.00</div>
    <ul style="top:159px">
      <li><svg width="13" height="13"><circle cx="6.5" cy="6.5" r="5" fill="none" stroke="#e0a93a" stroke-width="3"/></svg>Lorem ipsum dolor sit amet,</li>
      <li><svg width="13" height="13"><circle cx="6.5" cy="6.5" r="5" fill="none" stroke="#e0a93a" stroke-width="3"/></svg>Consectetur adipiscing elit, sed do</li>
      <li><svg width="13" height="13"><circle cx="6.5" cy="6.5" r="5" fill="none" stroke="#e0a93a" stroke-width="3"/></svg>Eiusmod tempor incididunt ut</li>
      <li><svg width="13" height="13"><circle cx="6.5" cy="6.5" r="5" fill="none" stroke="#e0a93a" stroke-width="3"/></svg>Labore et dolore magna aliqua.</li>
      <li><svg width="13" height="13"><circle cx="6.5" cy="6.5" r="5" fill="none" stroke="#e0a93a" stroke-width="3"/></svg>Ut enim ad minim veniam, nostrud</li>
      <li><svg width="13" height="13"><circle cx="6.5" cy="6.5" r="5" fill="none" stroke="#e0a93a" stroke-width="3"/></svg>Exercitation ullamco laboris</li>
      <li><svg width="13" height="13"><circle cx="6.5" cy="6.5" r="5" fill="none" stroke="#e0a93a" stroke-width="3"/></svg>Nisi ut aliquip ex ea commodo</li>
      <li><svg width="13" height="13"><circle cx="6.5" cy="6.5" r="5" fill="none" stroke="#e0a93a" stroke-width="3"/></svg>consequat. Duis aute irure dolor in</li>
    </ul>
  </div>
  <div class="pkg featured" style="left:447px;top:2466px;height:457px">
    <div class="pkg-head">DELUXE</div>
    <div class="price" style="top:96px">$150.00</div>
    <ul style="top:156px">
      <li><svg width="13" height="13"><circle cx="6.5" cy="6.5" r="5" fill="none" stroke="#e0a93a" stroke-width="3"/></svg>Lorem ipsum dolor sit amet,</li>
      <li><svg width="13" height="13"><circle cx="6.5" cy="6.5" r="5" fill="none" stroke="#e0a93a" stroke-width="3"/></svg>Consectetur adipiscing elit, sed do</li>
      <li><svg width="13" height="13"><circle cx="6.5" cy="6.5" r="5" fill="none" stroke="#e0a93a" stroke-width="3"/></svg>Eiusmod tempor incididunt ut</li>
      <li><svg width="13" height="13"><circle cx="6.5" cy="6.5" r="5" fill="none" stroke="#e0a93a" stroke-width="3"/></svg>Labore et dolore magna aliqua.</li>
      <li><svg width="13" height="13"><circle cx="6.5" cy="6.5" r="5" fill="none" stroke="#e0a93a" stroke-width="3"/></svg>Ut enim ad minim veniam, nostrud</li>
      <li><svg width="13" height="13"><circle cx="6.5" cy="6.5" r="5" fill="none" stroke="#e0a93a" stroke-width="3"/></svg>Exercitation ullamco laboris</li>
      <li><svg width="13" height="13"><circle cx="6.5" cy="6.5" r="5" fill="none" stroke="#e0a93a" stroke-width="3"/></svg>Nisi ut aliquip ex ea commodo</li>
      <li><svg width="13" height="13"><circle cx="6.5" cy="6.5" r="5" fill="none" stroke="#e0a93a" stroke-width="3"/></svg>consequat. Duis aute irure dolor in</li>
    </ul>
  </div>
  <div class="pkg" style="left:778px;top:2484px;height:423px">
    <div class="pkg-head">ULTIMATE</div>
    <div class="price" style="top:96px">$220.00</div>
    <ul style="top:159px">
      <li><svg width="13" height="13"><circle cx="6.5" cy="6.5" r="5" fill="none" stroke="#e0a93a" stroke-width="3"/></svg>Lorem ipsum dolor sit amet,</li>
      <li><svg width="13" height="13"><circle cx="6.5" cy="6.5" r="5" fill="none" stroke="#e0a93a" stroke-width="3"/></svg>Consectetur adipiscing elit, sed do</li>
      <li><svg width="13" height="13"><circle cx="6.5" cy="6.5" r="5" fill="none" stroke="#e0a93a" stroke-width="3"/></svg>Eiusmod tempor incididunt ut</li>
      <li><svg width="13" height="13"><circle cx="6.5" cy="6.5" r="5" fill="none" stroke="#e0a93a" stroke-width="3"/></svg>Labore et dolore magna aliqua.</li>
      <li><svg width="13" height="13"><circle cx="6.5" cy="6.5" r="5" fill="none" stroke="#e0a93a" stroke-width="3"/></svg>Ut enim ad minim veniam, nostrud</li>
      <li><svg width="13" height="13"><circle cx="6.5" cy="6.5" r="5" fill="none" stroke="#e0a93a" stroke-width="3"/></svg>Exercitation ullamco laboris</li>
      <li><svg width="13" height="13"><circle cx="6.5" cy="6.5" r="5" fill="none" stroke="#e0a93a" stroke-width="3"/></svg>Nisi ut aliquip ex ea commodo</li>
      <li><svg width="13" height="13"><circle cx="6.5" cy="6.5" r="5" fill="none" stroke="#e0a93a" stroke-width="3"/></svg>consequat. Duis aute irure dolor in</li>
    </ul>
  </div>
  <div class="buy">Buy Now
    <svg width="14" height="14" viewBox="0 0 16 16"><circle cx="8" cy="8" r="8" fill="var(--ink)"/><path d="M6 4.5L9.5 8 6 11.5" stroke="#fff" stroke-width="2" fill="none"/></svg>
  </div>

  <section class="reviews">
    <svg class="abs" style="left:0;top:0" width="1200" height="140">
      <polygon points="0,0 600,128 1200,0" fill="var(--green)"/>
      <polygon points="0,-14 600,114 1200,-14" fill="#fff"/>
    </svg>
    <h2 class="section-title serif">Trust Our Customer</h2>
    <div class="title-rule" style="top:228px"></div>

    <div class="review" style="left:111px">
      <div class="stars"><svg width="90" height="15" viewBox="0 0 90 15"><g fill="#f5b400"><path id="st" d="M7.5 0l2.2 4.8 5.3.6-3.9 3.6 1 5.2-4.6-2.6-4.6 2.6 1-5.2L0 5.4l5.3-.6z"/><use href="#st" x="18"/><use href="#st" x="36"/><use href="#st" x="54"/><use href="#st" x="72"/></g></svg></div>
      <span class="review-mark"></span>
      <p>Lorem ipsum dolor sit amet, consectetur adipiscing elit, sed do eiusmod tempor incididunt ut labore et dolore magna ad minim enim veniam aliqua.</p>
      <div class="reviewer"><div class="avatar" role="img" aria-label="Customer portrait"></div><div><b>Marcus Ellery</b><span>22 March 2024</span></div></div>
    </div>
    <div class="review" style="left:443px">
      <div class="stars"><svg width="90" height="15" viewBox="0 0 90 15"><g fill="#f5b400"><use href="#st"/><use href="#st" x="18"/><use href="#st" x="36"/><use href="#st" x="54"/><use href="#st" x="72"/></g></svg></div>
      <span class="review-mark"></span>
      <p>Lorem ipsum dolor sit amet, consectetur adipiscing elit, sed do eiusmod tempor incididunt ut labore et dolore magna ad minim enim veniam aliqua.</p>
      <div class="reviewer"><div class="avatar" role="img" aria-label="Customer portrait"></div><div><b>Tomas Reid</b><span>22 March 2024</span></div></div>
    </div>
    <div class="review" style="left:774px">
      <div class="stars"><svg width="90" height="15" viewBox="0 0 90 15"><g fill="#f5b400"><use href="#st"/><use href="#st" x="18"/><use href="#st" x="36"/><use href="#st" x="54"/><use href="#st" x="72"/></g></svg></div>
      <span class="review-mark"></span>
      <p>Lorem ipsum dolor sit amet, consectetur adipiscing elit, sed do eiusmod tempor incididunt ut labore et dolore magna ad minim enim veniam aliqua.</p>
      <div class="reviewer"><div class="avatar" role="img" aria-label="Customer portrait"></div><div><b>Delphine</b><span>22 March 2024</span></div></div>
    </div>
  </section>

  <section class="contact">
    <div class="map" role="img" aria-label="Map of the service area"></div>
    <div class="eyebrow" style="left:810px;top:3631px">CONTACT US</div>
    <h2 class="serif">Get in <span class="gold">Touch</span></h2>
    <div class="info" style="top:3720px">
      <svg width="30" height="30" viewBox="0 0 30 30"><path d="M15 1l12 5v9c0 7-5 12-12 14C8 27 3 22 3 15V6z" fill="none" stroke="var(--green)" stroke-width="1.5"/><path d="M15 8a4.5 4.5 0 0 0-4.5 4.5c0 3.5 4.5 8 4.5 8s4.5-4.5 4.5-8A4.5 4.5 0 0 0 15 8z" fill="var(--green)"/><circle cx="15" cy="12.5" r="1.6" fill="#fff"/></svg>
      <div><small>Location:</small>28 Harbor Lane, 47 W 9th Ave, Westbrook,<br>NY 10422</div>
    </div>
    <div class="info" style="top:3797px">
      <svg width="30" height="30" viewBox="0 0 30 30"><path d="M15 1l12 5v9c0 7-5 12-12 14C8 27 3 22 3 15V6z" fill="none" stroke="var(--green)" stroke-width="1.5"/><path d="M11 10c1-1 2 0 2.5 1.5s-1 1.5-.5 2.5 2 2.5 3 3 1.2-1.2 2.5-.6 2 1.3 1.2 2.2c-2 2-5 0-7-2s-3.4-5-1.7-6.6z" fill="var(--green)"/></svg>
      <div><small>Phone:</small><span style="font-size:17px">(555) 390 6612</span></div>
    </div>
    <div class="info" style="top:3862px">
      <svg width="30" height="30" viewBox="0 0 30 30"><path d="M15 1l12 5v9c0 7-5 12-12 14C8 27 3 22 3 15V6z" fill="var(--green)"/><rect x="9" y="11" width="12" height="8" fill="#fff"/><path d="M9 11l6 5 6-5" stroke="var(--green)" stroke-width="1.3" fill="none"/></svg>
      <div><small>Email:</small><u>info@halcyragloss.com</u></div>
    </div>
    <div class="btn-gold">Schedule an Appointment</div>
  </section>

  <footer class="footer">
    <div class="copy">Copyright © 2024 <span>Halcyra Gloss</span>. All Rights Reserved</div>
    <div class="follow">Follow us on:
      <span class="social"></span><span class="social"></span><span class="social"></span><span class="social"></span>
    </div>
  </footer>

</div>
</body>
</html>
```